Trade Show Banners

We would like to have a banner made to use at a Tradeshow. We provide Managed IT Services (locate at top of banner), Business VoIP (locate in middle), and Business Internet (locate at bottom). Attached is a "mock-up" and an image for the phone we would like to use. Please use your discretion for the other images. Below is the text for each section we would like included.

Title: Unleash the Power of Local IT Solutions

IT Services That Mean Business
Experience fanatical customer service with our affordable, full-service IT solutions. We’re 100% local, ensuring leading response times and personalized support—so you can focus on what you do best.

Talk More, Worry Less with Our Telephone Services
Say goodbye to overpriced equipment and hello to our free phone plan. Keep your number and enjoy unlimited local and long-distance calling. Tailor your phone system to your business needs and rest assured—our rates are always the lowest in town.

Highspeed Internet That Sets You Apart
Stay connected with blazing-fast speeds—from 1Gbps to 10Gbps, both up and down. Benefit from a static IP address and unbeatable prices, backed by 100% local support. Get the connectivity your business deserves at the best value in town.

Elevate your business with cutting-edge technology.

```html
<!DOCTYPE html>
<html lang="en">
<head>
<meta charset="utf-8">
<title>Northbyte Trade Show Banner</title>
<link rel="stylesheet" href="https://fonts.googleapis.com/css2?family=Bebas+Neue&family=Montserrat:wght@400;600;800&display=swap">
<style>
  :root {
    --stage: #d4d4d6;
    --white: #f2f2f2;
    --navy: #2b2f86;
    --navy-deep: #151a44;
    --indigo: #2f33a3;
    --indigo-bright: #3a42b4;
    --mint: #43c98e;
    --orange: #ef8f24;
    --text-light: #ffffff;
    --phone-dark: #2c3038;
    --phone-mid: #4a505c;
  }
  * { box-sizing: border-box; margin: 0; padding: 0; }
  html, body {
    width: 1103px;
    height: 1200px;
    overflow: hidden;
    background: var(--stage);
  }
  .banner {
    position: absolute;
    left: 314px;
    top: 30px;
    width: 474px;
    height: 1140px;
    overflow: hidden;
    background:
      radial-gradient(ellipse 180px 130px at 100% 100%, rgba(67, 201, 142, 0.95), rgba(67, 201, 142, 0) 80%),
      linear-gradient(135deg, rgba(255,255,255,0) 62%, rgba(255,255,255,0.04) 62%, rgba(255,255,255,0.04) 78%, rgba(255,255,255,0) 78%),
      linear-gradient(120deg, var(--navy-deep) 0%, #262a7a 35%, var(--indigo) 70%, var(--indigo-bright) 100%);
  }
  .banner__header {
    position: absolute;
    left: 0; top: 0;
    width: 100%;
    height: 217px;
    background: var(--white);
    display: flex;
    align-items: center;
    justify-content: center;
  }
  .brand-name {
    font-family: "Montserrat", sans-serif;
    font-weight: 800;
    font-size: 68px;
    letter-spacing: -2px;
    color: var(--navy);
    line-height: 1;
    text-transform: lowercase;
  }
  .display {
    font-family: "Bebas Neue", sans-serif;
    font-weight: 400;
    line-height: 1;
    text-align: center;
    position: absolute;
    left: 0;
    width: 100%;
    white-space: nowrap;
  }
  .accent { color: var(--orange); }
  .light { color: var(--text-light); }
  .headline-top { top: 263px; font-size: 56px; letter-spacing: -0.5px; }
  .headline-bottom { top: 317px; font-size: 58px; letter-spacing: -0.3px; }
  .product-art {
    position: absolute;
    left: 94px;
    top: 409px;
    width: 286px;
    height: 245px;
  }
  .services {
    position: absolute;
    left: 0;
    top: 702px;
    width: 100%;
    height: 95px;
  }
  .service {
    position: absolute;
    top: 0;
    width: 200px;
    font-family: "Bebas Neue", sans-serif;
    text-align: center;
    line-height: 1;
  }
  .service--it { left: 29px; }
  .service--voip { left: 247px; }
  .service__line { display: block; font-size: 46px; }
  .service__line + .service__line { margin-top: 5px; }
  .services__divider {
    position: absolute;
    left: 248px;
    top: 0;
    width: 2px;
    height: 90px;
    background: linear-gradient(to bottom, rgba(255,255,255,0), rgba(255,255,255,0.85) 30%, rgba(255,255,255,0.85) 70%, rgba(255,255,255,0));
  }
  .service-internet { top: 833px; font-size: 46px; }
  .contact {
    position: absolute;
    left: 62px;
    top: 958px;
    width: 344px;
    height: 68px;
    border: 1.5px solid var(--orange);
  }
  .contact__label {
    position: absolute;
    top: -9px;
    left: 50%;
    transform: translateX(-50%);
    padding: 0 5px;
    background: #2b2f86;
    font-family: "Montserrat", sans-serif;
    font-size: 14px;
    color: var(--text-light);
    line-height: 16px;
  }
  .contact__number {
    position: absolute;
    top: 9px;
    left: 0;
    width: 100%;
    text-align: center;
    font-family: "Bebas Neue", sans-serif;
    font-size: 55px;
    line-height: 1;
    color: var(--text-light);
  }
  .contact__web {
    position: absolute;
    bottom: -9px;
    left: 50%;
    transform: translateX(-50%);
    padding: 0 8px;
    background: #2c3088;
    font-family: "Montserrat", sans-serif;
    font-size: 13px;
    line-height: 16px;
    color: var(--text-light);
    white-space: nowrap;
  }
  .contact__web strong { font-weight: 600; }
</style>
</head>
<body>
  <main class="banner">
    <header class="banner__header">
      <span class="brand-name">Northbyte</span>
    </header>

    <h1 class="display headline-top light">Unleash the Power</h1>
    <p class="display headline-bottom accent">Of Local IT Solutions</p>

    <svg class="product-art" viewBox="0 0 286 245">
      <polygon points="0,0 223,0 0,216" fill="var(--white)"/>
      <defs>
        <linearGradient id="deskPhoneTone" x1="0" y1="0" x2="1" y2="1">
          <stop offset="0" stop-color="var(--phone-mid)"/>
          <stop offset="1" stop-color="var(--phone-dark)"/>
        </linearGradient>
      </defs>
      <rect x="30" y="21" width="256" height="224" rx="10" fill="url(#deskPhoneTone)" role="img" aria-label="Photo of a business VoIP desk phone with handset and colour screen"/>
    </svg>

    <section class="services">
      <div class="service service--it">
        <span class="service__line light">Managed</span>
        <span class="service__line accent">IT Services</span>
      </div>
      <div class="services__divider"></div>
      <div class="service service--voip">
        <span class="service__line light">Business</span>
        <span class="service__line accent">VoIP</span>
      </div>
    </section>

    <p class="display service-internet"><span class="light">Business</span> <span class="accent">Internet</span></p>

    <div class="contact">
      <span class="contact__label">Phone</span>
      <p class="contact__number">123-456-7890</p>
      <span class="contact__web">www.<strong>yourwebsite</strong>.com</span>
    </div>
  </main>
</body>
</html>
```